812 EDDM FLYER FOR CARPET CLEANING & WINDOW WASHING

Full Size Double Sided full color EDDM mailer

****PLEASE MAKE FONT TYPE, SIZE, COLOR, SPACING SAME AS IS EXAMPLE FLYER*******

***I have uploaded LOGO... It is on the VAN WRAP TIDYNORTH 812 HOME CARE

I have included an EDDM flyer and want my flyer to look like the example I uploaded.

I wanted to make it look Better & add my images and content. I have included the content under Must Haves......

Raindrop background

****Not all images will be used. Each service requires 2 images as seen on examply flyer... Please pic best 2 for each service, I can purchase new stock photo if needed

Target Market(s)

Residential Home Owners

Industry/Entity Type

Cleaning Service

Font styles to use
Serif

Colors
0555a3
ec1f27
fbed22
ffc214

Requirements
Must have
• Look Like Example EDDM postcard uploaded
• My images & content
• CARPET CLEANING Safe Eco-Friendly Truck Mounted Steam Cleaning. Say goodbye to those ugly carpet stains.
• WINDOW WASHING Interior/Exterior & Screens. Crystal Clear & Streak Free Windows
• POWER WASHING: Soft Wash & Power Wash. Safely cleans
• WATER DAMAGE: Got Mold or Water damage? Free IR Imaging Detection
• TILE & GROUT: Clean, Restore & Rejuvenate Tile, Grout & Stone
• MAINTENANCE: Professional & dependable repairs. We can Fit It!
• Call Today! 858-555-0147
• www.TidyNorth812.example
• ECO FRIENDLY CLEANING
• San Diego’s Trusted Cleaning Specialists

```html
<!DOCTYPE html>
<html lang="en">
<head>
<meta charset="utf-8">
<title>TidyNorth 812 Home Care – EDDM Flyer</title>
<link rel="stylesheet" href="https://fonts.googleapis.com/css2?family=Arimo:wght@700&family=Exo+2:ital,wght@1,800;1,900&family=Oswald:wght@500&family=Tinos:wght@700&display=swap">
<style>
  :root {
    --page: #d9dde3;
    --drop-light: #3a86d6;
    --drop-deep: #1c4fa6;
    --band-light: #0a68b4;
    --band-dark: #283b8d;
    --navy: #2b3a8c;
    --white: #ffffff;
    --tag: rgba(220, 222, 255, 0.78);
    --photo-warm: #d9d3cc;
  }
  * { box-sizing: border-box; margin: 0; padding: 0; }
  html, body { width: 1200px; height: 1200px; overflow: hidden; background: var(--page); }
  .flyer {
    position: absolute; left: 0; top: 150px;
    width: 1200px; height: 900px; overflow: hidden;
    font-family: "Exo 2", sans-serif;
  }
  .flyer__raindrops {
    position: absolute; inset: 0;
    background: radial-gradient(circle at 50% 40%, var(--drop-light), var(--drop-deep));
  }
  .headline-band { position: absolute; left: 0; width: 1200px; top: 72px; height: 228px;
    border-top: 3px solid var(--white); border-bottom: 3px solid var(--white);
    background: linear-gradient(var(--band-light) 0 56%, var(--band-dark) 56% 100%); }
  .pill {
    position: absolute; display: flex; align-items: center; justify-content: center;
    border: 3px solid var(--white); border-radius: 40px;
    font-style: italic; font-weight: 900; letter-spacing: 0.5px;
  }
  .pill--offer { left: 228px; top: 36px; width: 740px; height: 78px; background: var(--navy); color: var(--white); font-size: 40px; }
  .pill--services { left: 230px; top: 258px; width: 736px; height: 74px; background: var(--white); border-color: var(--navy); color: var(--navy); font-size: 50px; }
  .headline {
    position: absolute; left: 0; width: 1200px; top: 124px; text-align: center;
    font-family: "Arimo", sans-serif; font-weight: 700; font-size: 117px; line-height: 1;
    color: var(--white); letter-spacing: -1px; text-shadow: 3px 3px 4px rgba(20, 30, 90, 0.6);
  }
  .services {
    position: absolute; left: 76px; top: 343px; width: 1044px; height: 369px;
    display: grid; grid-template-columns: repeat(3, 1fr); grid-template-rows: repeat(2, 1fr);
    gap: 1px; background: var(--white);
  }
  .service { position: relative; }
  .service__photo { position: absolute; inset: 0; }
  .service__label {
    position: absolute; left: 0; right: 0; bottom: 22px; text-align: center;
    font-style: italic; font-weight: 900; font-size: 30px; color: var(--navy);
    letter-spacing: -0.5px;
    text-shadow: -2px -2px 0 var(--white), 2px -2px 0 var(--white), -2px 2px 0 var(--white), 2px 2px 0 var(--white), 0 3px 5px rgba(0,0,0,0.4);
  }
  .service:nth-child(-n+3) .service__label { bottom: 20px; }
  .brand {
    position: absolute; left: 44px; top: 762px; display: flex; align-items: center; gap: 16px;
    font-family: "Exo 2", sans-serif; font-style: italic; font-weight: 900; font-size: 34px;
    line-height: 1.05; color: var(--white);
  }
  .brand__dot { width: 70px; height: 70px; border-radius: 50%; background: var(--white); flex: none; }
  .call-today {
    position: absolute; left: 470px; top: 706px; transform: rotate(-22deg);
    font-style: italic; font-weight: 800; font-size: 30px; color: var(--white);
    text-shadow: 0 2px 3px rgba(0,0,0,0.4);
  }
  .contact { position: absolute; left: 495px; top: 752px; width: 462px; text-align: center; color: var(--white); }
  .contact__phone { font-family: "Tinos", serif; font-weight: 700; font-size: 72px; line-height: 1; text-shadow: 2px 3px 4px rgba(0,0,0,0.5); }
  .contact__web { font-family: "Tinos", serif; font-weight: 700; font-size: 21px; letter-spacing: 1.5px; margin-top: 6px; }
  .contact__tagline { font-family: "Oswald", sans-serif; font-weight: 500; font-size: 22px; margin-top: 2px; letter-spacing: 0.4px; }
  .back-tag { position: absolute; left: 965px; top: 765px; width: 200px; height: 106px; }
  .back-tag__text { position: absolute; inset: 0; padding: 22px 30px 0 12px; text-align: center; color: var(--navy); }
  .back-tag__title { font-family: "Arimo", sans-serif; font-weight: 700; font-size: 20px; letter-spacing: -0.5px; }
  .back-tag__sub { font-style: italic; font-weight: 800; font-size: 15px; line-height: 1.05; color: var(--white); margin-top: 6px; padding-left: 20px; }
</style>
</head>
<body>
<main class="flyer">
  <div class="flyer__raindrops" role="img" aria-label="Water droplets on a blue surface"></div>

  <div class="headline-band"></div>
  <div class="pill pill--offer">Don’t Mess Out! We’re Offering:</div>
  <h1 class="headline">FREE ESTIMATES</h1>
  <div class="pill pill--services">On All of Our Services!</div>

  <section class="services">
    <div class="service">
      <div class="service__photo" role="img" aria-label="Child and puppy resting on a clean carpet" style="background: linear-gradient(135deg, #eef1f3, #c9c8c2);"></div>
      <h2 class="service__label">CARPET CLEANING</h2>
    </div>
    <div class="service">
      <div class="service__photo" role="img" aria-label="Worker squeegeeing a window" style="background: linear-gradient(135deg, #dfe6ee, #7f98b3);"></div>
      <h2 class="service__label">WINDOW WASHING</h2>
    </div>
    <div class="service">
      <div class="service__photo" role="img" aria-label="Pressure washer cleaning a brick paver patio" style="background: linear-gradient(135deg, #b88a80, #9c5b52);"></div>
      <h2 class="service__label">POWER WASHING</h2>
    </div>
    <div class="service">
      <div class="service__photo" role="img" aria-label="Mold stain spreading on a white wall" style="background: linear-gradient(135deg, #a39a8e, #eceef2);"></div>
      <h2 class="service__label">WATER DAMAGE</h2>
    </div>
    <div class="service">
      <div class="service__photo" role="img" aria-label="Hand spreading grout on floor tile with a float" style="background: linear-gradient(135deg, #c7bba6, var(--photo-warm));"></div>
      <h2 class="service__label">TILE &amp; GROUT</h2>
    </div>
    <div class="service">
      <div class="service__photo" role="img" aria-label="Painter on a ladder rolling a white wall" style="background: linear-gradient(135deg, #f2f4f6, #c9d3de);"></div>
      <h2 class="service__label">MAINTENANCE</h2>
    </div>
  </section>

  <div class="brand">
    <span class="brand__dot"></span>
    <span>TIDYNORTH 812<br>HOME CARE</span>
  </div>

  <div class="call-today">Call Today</div>
  <div class="contact">
    <div class="contact__phone">858-555-0147</div>
    <div class="contact__web">WWW.TIDYNORTH812.EXAMPLE</div>
    <div class="contact__tagline">SAN DIEGO’S TRUSTED CLEANING SPECIALISTS</div>
  </div>

  <div class="back-tag">
    <svg width="200" height="106" viewBox="0 0 200 106" aria-hidden="true">
      <polygon points="0,0 166,0 200,53 166,106 0,106" fill="var(--tag)"/>
    </svg>
    <div class="back-tag__text">
      <div class="back-tag__title">LOOK ON BACK</div>
      <div class="back-tag__sub">to see what we<br>can do for you!</div>
    </div>
  </div>
</main>
</body>
</html>
```